Wordpress Design Project

I now need a Wordpress theme for my new business.
The business offers consultancy on Information Management, Knowledge Management, Records Management and Document Management.
The winning designer must be able to set up the site for me on my webspace provided by Tallowbrook Hosting, or talk me through how to do this.
I already have a logo designed which you can see by viewing my profile on here. I am happy to send copies of the original artwork to bidders.
I recently sold my interest in a very similar business, and want a website similar to (but not the same as) the previous company (who are now my competition!) This website can be viewed at www.qardvane.com
Categories will be similar, but I would like everything to be as configurable as possible.
I have a strong preference for clean unfussy design.
I want original design please. Please no templates from free to use sites with stock images... no jigsaw pictures!!!!
Love this one... http://www.felquist.tv/
Please get in touch with any questions.
Updates
Project Deadline Extended
Reason: All of these are too generic (brief says no jigsaw puzzle images), or have copied QDV which is the COMPETITION - so I don't want the site to look like theirs
Project Deadline Extended
Reason: Please keep trying people
Business
Business

```html
<!DOCTYPE html>
<html lang="en">
<head>
<meta charset="utf-8">
<title>Harwick Professional Services</title>
<link rel="stylesheet" href="https://fonts.googleapis.com/css2?family=Arimo:ital,wght@0,400;1,400&display=swap">
<style>
:root{
  --page:#97c8df;
  --header:#72b5d4;
  --header-sweep:#86c1dc;
  --nav:#5eaed0;
  --nav-line:#3f88ab;
  --tab:#8fc3db;
  --tab-active:#a9d4e7;
  --tab-border:#5a9dbf;
  --ink:#111d24;
  --brand:#1f2a63;
  --meta-bar:#a9d4e7;
  --meta-ink:#2b4a58;
  --link:#2c6d85;
  --visited:#4b7b8e;
  --hover:#1ab3dc;
  --photo-a:#e4eef6;
  --photo-b:#7f9fbd;
  --input:#ffffff;
}
*{margin:0;padding:0;box-sizing:border-box}
html,body{width:1200px;height:900px;overflow:hidden}
body{background:var(--page);font-family:"Arimo",Arial,sans-serif;color:var(--ink);position:relative}
.site-header{position:absolute;left:0;top:0;width:1200px;height:193px;background:var(--header);overflow:hidden}
.site-header .sweep{position:absolute;left:0;top:0}
.brand{position:absolute;left:215px;top:36px;display:flex;align-items:center;gap:28px;color:var(--brand)}
.brand-dot{width:146px;height:146px;border-radius:50%;background:var(--brand)}
.brand-name{font-weight:400;letter-spacing:5px;line-height:1}
.brand-name .word{display:block;font-size:66px;letter-spacing:6px}
.brand-name .tag{display:block;font-size:21px;letter-spacing:6.2px;margin-top:14px}
.main-nav{position:absolute;left:0;top:193px;width:1200px;height:45px;background:var(--nav);border-bottom:1px solid var(--nav-line)}
.main-nav ul{list-style:none;position:absolute;left:265px;top:15px;display:flex;gap:11px}
.main-nav a{display:block;height:30px;padding:0 21px;line-height:29px;font-size:14px;color:#14323f;text-decoration:none;background:var(--tab);border:1px solid var(--tab-border);border-bottom:none}
.main-nav .current a{background:var(--tab-active);height:30px}
.post{position:absolute;left:286px;top:268px;width:494px}
.post-title{font-size:26px;font-weight:400;line-height:32px;display:flex;align-items:center;gap:8px;color:#1a3440}
.post-title .bullet{width:24px;height:24px;border-radius:50%;background:radial-gradient(circle at 40% 30%,#8fb8c4,#1d4a58 70%)}
.post-title a{color:#1a3440}
.post-title .hovered{color:var(--hover)}
.post-meta{height:19px;background:var(--meta-bar);font-size:12px;font-style:italic;color:var(--meta-ink);line-height:19px;padding-left:3px}
.post-body{margin-top:17px;font-size:14px;line-height:16px;text-align:justify}
.post-body p{margin-bottom:12px}
.photo{float:left;width:370px;height:264px;margin:0 5px 0 5px;background:linear-gradient(150deg,var(--photo-a),var(--photo-b))}
.badge{float:left;width:54px;height:54px;margin:0 6px 4px 4px;border-radius:50%;background:#2f6c95;border:3px solid #e8f1f6}
.post-body sup,.post-body sub{font-size:12px}
.post-body a{color:var(--link);text-decoration:none}
.post-body a.visited{color:var(--visited)}
.post-body a.hovered{color:var(--hover);text-decoration:underline}
.post-footer{font-size:12px;font-style:italic;color:var(--meta-ink);padding-left:2px;margin-top:-2px}
.post-footer .hovered{color:var(--link);text-decoration:underline}
.sidebar{position:absolute;left:824px;top:259px;width:191px}
.widget-title{font-size:14px;font-weight:400;color:#1a3440;display:flex;align-items:center;gap:6px;padding-left:3px}
.widget-title .square{width:8px;height:8px;border:1px solid #1a3440;background:var(--tab-active)}
.search-field{margin-top:16px;height:22px;background:var(--input);border:1px solid #7fb0c8;position:relative}
.search-field svg{position:absolute;right:1px;top:2px}
</style>
</head>
<body>
<header class="site-header">
  <svg class="sweep" width="1200" height="193" viewBox="0 0 1200 193" aria-hidden="true">
    <path d="M220 0 C520 40 900 60 1200 62 L1200 0 Z" fill="var(--header-sweep)"/>
    <path d="M600 0 C820 30 1000 45 1200 40 L1200 0 Z" fill="#63add0" opacity=".5"/>
  </svg>
  <div class="brand">
    <div class="brand-dot"></div>
    <div class="brand-name"><span class="word">HARWICK</span><span class="tag">PROFESSIONAL SERVICES</span></div>
  </div>
</header>
<nav class="main-nav">
  <ul>
    <li class="current"><a href="#">HOME</a></li>
    <li><a href="#">MENU ITEM</a></li>
    <li><a href="#">ABOUT</a></li>
  </ul>
</nav>
<article class="post">
  <h1 class="post-title"><span class="bullet"></span><span>TEXT, <a href="#">LINK</a>, VISITED, <a class="hovered" href="#">HOVERED</a></span></h1>
  <div class="post-meta">Published November 05, 2008 | By admin | Edit</div>
  <div class="post-body">
    <p><span class="photo" role="img" aria-label="Photo of a bright glass-roofed atrium with curved steel beams"></span><span class="badge" role="img" aria-label="Round site badge"></span>Lorem <sup>superscript</sup> dolor <sub>subscript</sub> amet, consectetuer adipiscing <a href="#">link</a>, <a class="visited" href="#">visited link</a>, <a class="hovered" href="#">hovered link</a> consectetuer adipiscing elit. Quisque sed felis. Aliquam sit amet felis. Mauris semper, velit semper laoreet dictum, quam diam dictum urna, nec placerat elit nisl <a href="#">one more link</a> in quam. Etiam augue pede, molestie eget, rhoncus at, convallis ut, eros.</p>
    <p>Aliquam pharetra. Nulla in tellus eget odio sagittis blandit.Maecenas at nisl. Nullam lorem mi, eleifend a, fringilla vel, semper at, ligula. Mauris eu wisi. Ut ante dui, aliquet nec, congue non, accumsan sit amet, lectus. Mauris et mauris. Duis sed massa id mauris pretium venenatis. Suspendisse cursus velit vel ligula. Mauris elit.</p>
    <p>Aliquam pharetra. Nulla in tellus eget odio sagittis blandit.Maecenas at nisl. Nullam lorem mi, eleifend a, fringilla vel, semper at, ligula. Mauris eu wisi. Ut ante dui, aliquet nec, congue non, accumsan sit amet, lectus. Mauris et mauris. Duis sed massa id mauris pretium venenatis. Suspendisse cursus velit vel ligula. Mauris elit.</p>
  </div>
  <div class="post-footer">Category: No Category | Tags: link, visited, <span class="hovered">hovered</span> | No Comments »</div>
</article>
<aside class="sidebar">
  <h2 class="widget-title"><span class="square"></span>SEARCH</h2>
  <div class="search-field">
    <svg width="16" height="16" viewBox="0 0 16 16" aria-hidden="true"><circle cx="6.5" cy="6.5" r="4.5" fill="none" stroke="#8a9aa3" stroke-width="1.4"/><path d="M10 10 L14 14" stroke="#8a9aa3" stroke-width="2"/></svg>
  </div>
</aside>
</body>
</html>
```